Cutting edge/Modern brochure for #1 Indie real estate brokerage in the area.

Professional/Modern looking marketing brochures that we can leave behind after a listing or buyer presentation. We are the #1 local Indie Real Estate Company and a group of top producing agents broke away from the corporate real estate world. We just opened our second location which is 6,000 sq ft and a very modern design. Our website is www.pelvarhouses.com and our facebook page Tarnish Oak Real Estate Services has a sneak peak commercial of the new office to get inspiration. Attached is a file with verbiage and our logo with a black background and one with no background. We have cutting edge technology, offer 3D spherevue technology with virtual tours, radio show, etc...We want these pieces to be powerful to make the clients want to choose us!

Target Market(s)

We would like a brochure for buyers and one for sellers

Industry/Entity Type

Real Estate

Colors

Designer to choose colors to be used in the design.

Requirements
Must have
• Sleek, modern, professional look

```html
<!DOCTYPE html>
<html lang="en">
<head>
<meta charset="utf-8">
<title>Tarnish Oak Real Estate Services – Brochure</title>
<link href="https://fonts.googleapis.com/css2?family=Brawler&display=swap" rel="stylesheet">
<style>
:root{
  --slate:#6a6a6a;
  --tan:#c9b396;
  --cream:#f4f0ea;
  --body:#e6e1da;
  --sand:#b7a794;
  --sand-text:#f1e9de;
  --ink:#3f3f3f;
  --gold:#b8992a;
  --blush:#f4eeee;
  --tech-ink:#555;
}
*{margin:0;padding:0;box-sizing:border-box}
html,body{width:1200px;height:928px;overflow:hidden;background:#fff}
body{font-family:"Brawler",serif;font-weight:400;position:relative}
h2{font-weight:400}
.panel{position:absolute;top:0;height:928px;overflow:hidden}
.panel-about{left:0;width:400px;background:var(--slate);color:var(--cream)}
.panel-growth{left:400px;width:400px}
.panel-tech{left:800px;width:400px}

.block{position:absolute;left:15px}
.tagline{left:0;width:400px;text-align:center;font-size:16px;line-height:19px;color:#fff}
.section-title{left:0;width:400px;color:var(--tan);text-align:center;font-size:20.5px;line-height:22.7px}
.body-copy{width:355px;font-size:15px;line-height:18.3px;color:var(--body)}
.lead{width:385px;font-size:15.5px;line-height:18.5px;color:#fff}
.ticks{list-style:none;width:385px;font-size:15px;line-height:18.3px;color:var(--body)}
.ticks li::before{content:"‣";color:var(--tan);margin:0 9px 0 3px;font-size:11px}
.ticks-tight{margin-top:1px}

.photo-kitchen{position:absolute;left:0;top:0;width:400px;height:600px;background:linear-gradient(180deg,#e9e4dc 0%,#c9a27a 35%,#d8d2c8 65%,#cfc9c0 100%)}
.growth-band{position:absolute;left:0;top:600px;width:400px;height:328px;background:var(--sand)}
.growth-title{position:absolute;left:0;top:57px;width:400px;color:var(--sand-text);text-align:center;font-size:29px;line-height:34px}
.growth-lead{position:absolute;left:15px;top:104px;width:380px;color:var(--ink);font-size:21px;line-height:19px}
.growth-lead em{font-style:normal;color:var(--sand-text)}
.growth-stats{position:absolute;left:40px;top:156px;list-style:none;color:var(--sand-text);font-size:21px;line-height:23.5px}
.growth-stats li::before{content:"‣";color:#8a7c6c;margin-right:12px;font-size:13px}

.tech-copy{position:absolute;left:0;top:112px;width:400px;padding:0 6px 0 15px;color:var(--tech-ink)}
.tech-title{text-align:center;font-size:24px;line-height:27px;letter-spacing:-.2px;margin-bottom:5px}
.tech-list{list-style:none;font-size:21.5px;line-height:24.4px}
.tech-list li::before{content:"‣";color:#999;margin:0 10px 0 9px;font-size:12px}
.brand-band{position:absolute;left:0;top:425px;width:400px;height:170px;background:var(--blush);display:flex;flex-direction:column;align-items:center;justify-content:center}
.brand-name{color:var(--gold);font-size:38px;letter-spacing:1px;display:flex;align-items:center;gap:12px}
.brand-name .mark{width:14px;height:14px;background:var(--gold)}
.brand-sub{color:var(--gold);font-size:13px;letter-spacing:3px;margin-top:8px}
.photo-city{position:absolute;left:0;top:595px;width:400px;height:333px;background:linear-gradient(180deg,#d9c2c4 0%,#6d6a78 30%,#3c3a47 65%,#5a4c4c 100%)}
</style>
</head>
<body>
<section class="panel panel-about">
  <p class="block tagline" style="top:28px">We are the Area's #1 Indie Brokerage</p>
  <h2 class="block section-title" style="top:70px">Excellent Service that leads to Results!<br>Who is Tarnish Oak?</h2>
  <p class="block body-copy" style="top:127px">We are a team of top producing professionals with a passion to help make your vision and dreams come true. Our high standards provide excellent service and we will get you results, holding your hand every step of the way.</p>
  <p class="block body-copy" style="top:232px">Tarnish Oak encompasses award winning Realtors that are continually trained and apply the best of the best marketing plans, advertising materials and cutting-edge technology to ensure your home buying or selling experience is a success.</p>
  <h2 class="block section-title" style="top:356px">Premier Agent:<br>The Power of Homevista and Parcelry</h2>
  <div class="block" style="top:410px">
    <p class="lead">What is a Premier Agent?</p>
    <ul class="ticks ticks-tight">
      <li>Top 1% of all Realtors on Homevista and Parcelry</li>
      <li>230+ 5-Star Reviews</li>
    </ul>
  </div>
  <h2 class="block section-title" style="top:479px">NO ONE WILL WORK HARDER<br>FOR YOU!</h2>
  <p class="block lead" style="top:531px">100% OF OUR Premier Leaders are<br>FULL-TIME REALTORS</p>
  <ul class="block ticks" style="top:574px">
    <li>Dedication to our Careers = Dedication to you!</li>
    <li>We make ourselves available when you are!</li>
    <li>We PROMISE to make ourselves available to you via Phone, Text, and e-mail anytime you need us!</li>
  </ul>
  <div class="block" style="top:684px">
    <p class="lead">More Sales per Realtor than any other company</p>
    <ul class="ticks">
      <li>Tarnish Oak Agents – 31 Sales/year</li>
      <li>National Average – 10 Sales/year</li>
    </ul>
  </div>
  <div class="block" style="top:752px">
    <p class="lead">Why choose a single Realtor when you can have a team 40+ strong?</p>
    <ul class="ticks">
      <li>Unlike any other brokerage, we work together as a Team because Together We Achieve More! We have a family atmosphere that focuses on customer service.</li>
    </ul>
  </div>
</section>

<section class="panel panel-growth">
  <div class="photo-kitchen" role="img" aria-label="Photo of a modern galley kitchen with wood cabinets and a window at the end"></div>
  <div class="growth-band">
    <h2 class="growth-title">WE ARE GROWING!</h2>
    <p class="growth-lead">Since its founding in 2015 we have <em>doubled</em> our growth every year!</p>
    <ul class="growth-stats">
      <li>2015 - $15,955,929 (126 Sales)</li>
      <li>2016 - $30,464,637 (215 Sales)</li>
      <li>2017 - $61,093,429 (419 Sales)</li>
    </ul>
  </div>
</section>

<section class="panel panel-tech">
  <div class="tech-copy">
    <h2 class="tech-title">We Utilize the Latest Technology to make sure Your Home Sells Quickly and for Top Dollar at NO Additional cost to you!</h2>
    <ul class="tech-list">
      <li>SignTrail Electronic Documents and Signatures</li>
      <li>Spherevue 3D Virtual Tours</li>
      <li>Professional Listing Photos</li>
      <li>Aerial Drone Videos and Photos</li>
      <li>Radio Show</li>
      <li>Social Media</li>
    </ul>
  </div>
  <div class="brand-band">
    <div class="brand-name"><span class="mark"></span>Tarnish Oak</div>
    <div class="brand-sub">REAL ESTATE SERVICES</div>
  </div>
  <div class="photo-city" role="img" aria-label="Aerial photo of a city skyline at dusk"></div>
</section>
</body>
</html>
```